Business card design for a dynamic IT consulting company

We need a business card design for a young firm, specialized in the Telecommunications/Consulting industry. The name of the company is Brask and Partners Business Consulting Ltd. (Short name: Brask and Partnes)
Brask = solve read reverse, so we aim to be uncomplicated and solution-oriented. The small pipe in our logo is also related to the word solve. So we need a new business card design, which is simple, eye catching and something non traditional (I would probably prefer a square shaped design rather than a rectangle, but open for suggestions). Attached our logo.

Target Market(s)

Usually our customers are Tier1 Telecoms providers (Q-Linkra, Parnexo, etc) and their executives.

Industry/Entity Type

Business

Contact Information for Business Card

Name: Gergely Halmindo
Email: g.halmindo@braskpartnera.hu
Web: www.braskpartnera.hu
Mobile: +36 30 555 0192
Title: Managing Director

Optional:
Company name: Brask and Partners Ltd.
Address: 1047 Budapest, Ravaszi str. 17/B, Hungary

Font styles to use
Other font styles liked:
• helveticaneue_medium, Prime Regular are used now.

Colors

Designer to choose colors to be used in the design.

Requirements
Must have
• I would like to have a 2 sided design.
Nice to have
• I thought if we make the logo a bit bigger (without the company name), that could go to the back with the company name below. I though, if the pipe in the logo is somehow touchable on the business card, would be nice and unique.

```html
<!DOCTYPE html>
<html lang="en">
<head>
<meta charset="utf-8">
<title>Brask and Partners – Business Card</title>
<link rel="stylesheet" href="https://fonts.googleapis.com/css2?family=Open+Sans:wght@400&family=Arimo:wght@700&display=swap">
<style>
  :root{
    --stage:#e9e8e8;
    --black:#000000;
    --white:#ffffff;
    --red:#d91f26;
    --red-dark:#a8141a;
    --panel-top:#a3a3a3;
    --panel-bottom:#8c8c8c;
    --brand-front:#333333;
    --brand-back:#ffffff;
  }
  html,body{margin:0;padding:0;overflow:hidden;}
  body{width:1200px;height:1000px;background:var(--stage);position:relative;}
  .card{position:absolute;left:242px;width:758px;overflow:hidden;}
  .card--front{top:64px;height:433px;}
  .card--back{top:514px;height:432px;background:var(--black);}
  .card__shapes{position:absolute;left:0;top:0;}
  .brand{position:absolute;font-family:"Open Sans",sans-serif;font-weight:400;white-space:nowrap;letter-spacing:1px;}
  .brand--front{left:58px;top:208px;font-size:17px;color:var(--brand-front);}
  .brand--back{left:66px;top:196px;font-size:30px;color:var(--brand-back);}
  .person{position:absolute;left:382px;top:80px;color:var(--white);font-family:"Open Sans",sans-serif;}
  .person__name{margin:0;font-size:28px;font-weight:400;line-height:1.1;letter-spacing:.2px;}
  .person__title{margin:2px 0 0 2px;font-size:14px;line-height:1;}
  .contact{position:absolute;left:362px;width:396px;background:linear-gradient(var(--panel-top),var(--panel-bottom));}
  .contact--phone{top:144px;height:65px;}
  .contact--web{top:222px;height:64px;}
  .contact--address{top:297px;height:65px;}
  .contact__icon{position:absolute;left:26px;}
  .contact__text{position:absolute;left:88px;color:var(--white);font-family:Arimo,sans-serif;font-weight:700;font-size:19px;line-height:26px;white-space:nowrap;}
  .contact--phone .contact__text{top:19px;}
  .contact--web .contact__text{top:6px;font-size:18px;}
  .contact--address .contact__text{top:5px;left:86px;}
  .back-band{position:absolute;right:0;top:0;width:188px;height:100%;background:var(--red);}
</style>
</head>
<body>

<section class="card card--front" aria-label="Card front">
  <svg class="card__shapes" width="758" height="433" viewBox="0 0 758 433">
    <rect x="0" y="0" width="758" height="433" fill="var(--white)"/>
    <rect x="0" y="0" width="31" height="433" fill="var(--black)"/>
    <rect x="354" y="136" width="404" height="235" fill="var(--black)"/>
    <rect x="373" y="0" width="385" height="433" fill="var(--black)"/>
    <rect x="327" y="0" width="46" height="136" fill="var(--red)"/>
    <polygon points="327,136 354,136 354,190" fill="var(--red-dark)"/>
    <polygon points="354,318 354,371 327,371" fill="var(--red-dark)"/>
    <rect x="327" y="371" width="46" height="62" fill="var(--red)"/>
  </svg>

  <div class="brand brand--front">BRASK AND PARTNERS LTD.</div>

  <div class="person">
    <h1 class="person__name">GERGELY HALMINDO</h1>
    <p class="person__title">MANAGING DIRECTOR</p>
  </div>

  <div class="contact contact--phone">
    <svg class="contact__icon" style="top:10px" width="42" height="44" viewBox="0 0 42 44">
      <rect x="1" y="1" width="40" height="40" rx="5" fill="var(--black)"/>
      <path d="M14 9c-3 2-4 6-2 12s6 11 10 13c2 1 4 0 5-1l-4-6-3 1c-2-2-4-6-4-9l3-1-1-7z" fill="none" stroke="var(--white)" stroke-width="2.2" stroke-linejoin="round"/>
    </svg>
    <div class="contact__text">+36 30 555 0192</div>
  </div>

  <div class="contact contact--web">
    <svg class="contact__icon" style="top:11px" width="44" height="44" viewBox="0 0 44 44">
      <circle cx="22" cy="22" r="20" fill="var(--black)"/>
      <polygon points="11,13 34,22 11,31 16,22" fill="var(--white)"/>
    </svg>
    <div class="contact__text">g.halmindo@braskpartnera.hu<br>www.braskpartnera.hu</div>
  </div>

  <div class="contact contact--address">
    <svg class="contact__icon" style="top:10px;left:30px" width="32" height="46" viewBox="0 0 32 46">
      <path d="M16 2C8 2 2 8 2 16c0 10 14 28 14 28s14-18 14-28C30 8 24 2 16 2z" fill="var(--red)"/>
      <circle cx="16" cy="15" r="5" fill="#8f1016"/>
    </svg>
    <div class="contact__text">1047 Budapest,<br>Ravaszi str. 17/B, Hungary</div>
  </div>
</section>

<section class="card card--back" aria-label="Card back">
  <div class="back-band"></div>
  <div class="brand brand--back">BRASK AND PARTNERS LTD.</div>
</section>

</body>
</html>
```